Guarenteed! - Homepage Website Design - Coding not required- Winner to complete further pages

Hi all,

We're looking at redesigning our current website with a few adjustments to other pages but the main adjustments will be on the homepage which is what this design request is for. Please note : any of these ideas can be changed if you have something particularly different / special in mind etc.

P.S Coding is not required, just a design.

- Our website -

Our website is simply a price comparison website that allows customers to find companies within their area at the best price. The products available are mostly related to the vehicle trade and all refer to vinyl. This includes the likes of vehicle window tint, vehicle colour change vehicle wrap, vehicle signage as well as other cosmetic vinyl modifications. We allow the customer to search for their product within their chosen area and receive a list of companies who supply their product within that area. From here they can compare prices and view further details on the company.

- What we're looking to do -

We're looking first of all to adjust how the website homepage is displayed, this includes adding images and adjusting the colours that are explained below:

First of all, we look to spread out each of the 12 products (which can be seen on the website as it stands) and add an image to each of the products (all being spaced out as shown in our sketch)

We've been told the website looks too busy so we're thinking if we adjust the colours to more simplier neutral colours as well as the main focus of the website being on the 12 images, that would be great.

- Logo + Banner -

Logo to remain top left although banner may be removed / adjusted to make simplier.

- Colours -

Adjustments - Colours shades
We want the website to still look exciting but simplify the colours. Needs to be kept up to date with the colours / textures etc (bright colours to highlight keypoints)
We're still looking to use either blue or orange or maybe both to highlight these keypoints but the main website to be light colours and maybe even black on white background. The entire homepage can be adjusted colour wise if you feel it fits into your theme including menu bars, banners etc. The key is to get this right with being not too overpowering with the colours but still look interesting and up to date.

- 1 - 4 steps banner - (text may change)

This sits just under the logo and explains to the user how easy the website is to use and the steps they need to take. This may change to a 1 - 5 steps but we're looking to have this designed once the overall colours / theme of the website is sorted.

- 12 images - 4 x 3

This is the main focus of the website and will be the main focus of what the customer sees first of all. This will be where they select their product and then underneath, enter their postcode and distance they would like to search within. As explained further up, we have some of the product images available so if you can where possible add these to the design and then duplicate the images on those we currently don't have available.

- 12 Images -Titles -

These titles will be in this order from left to right and etc

- Colour Change Wrap
- Printed Vehicle Wrap
- Window Tint
- Headlight Tint
- Vehicle Signage
- Shop Signage
- Roof Vinyl Wrap
- Bonnet Vinyl Wrap
- Carbon Fibre Vinyl
- Stickerbomb Vinyl
- Clear Protective Vinyl
- Wheel Refurb

Text to be quite large, centered and with the o to the left of the title. Short titles like 'Window Tint' should fit on one line in the middle of the box where as titles such as ' Stickerbomb Vinyl Wrap' should have the 'Stickerbomb Vinyl' on the first line with the 'Wrap' on the line below. The background of this text is up to experient, might be worth just a simple colour or it might be worth using a bright blue or orange to keep in with the theme of the logo etc.

These will also have the circle tick box to the left of the title (as on the current website) where the customer clicks to select the product they have available.
We were also thinking that if when the customer ticks the circle on their selected box, the box is highlighted in some way to show this.

- Search Block -

This will appear under the 12 images and allows the customer to input their postcode and distance for the search criteria. Colours on this can of course be adjusted to keep in theme with the website.

- Under the 12 Images -

- Block underneath the 12 images and search block -

To the left will be some key bullet points about the website - maybe 4 or 5 with a green tick to the left of this. Background colour will probably be best to be a light colour, possibly grey.

Then to the right of this will appear 4 images, 2 before and 2 after when applying these products. Images to be used aren't fully decided on and we would like this stage of the design left to the end when the rest of the theme etc have been decided on.

Attached images are as follows :
- How the website looks as it stands
- The fold line on the website (obviously important)
- Our rough sketch of how we'd like the website homepage to look.
- We have 7 of the images ready that are all attached in this one file. Please duplicate the images on those that currently don't have the image available.

We will also be requesting a website developer to put this into action if our current designer falls through so please feel free to contact us if potentially interested.

The layout can change if you can think of something particular different / unique that works with this design. The main idea is to not only get the 12 products on view to the viewers but also the keypoints and before and after images.

Any questions, please ask away as we're bound to have forgotten a few things.

Thanks and good luck!

Hi all, keep the designs coming.

We haven't quite seen that extra special design we're after. As stated, we're after something fairly simple to suit the youth as well as the middle aged but we're also after something that bit special.

Colours to concentrate on are still and orange etc although feel free to use other colours if you have anything special in mind.

Please experience and we'll give you our honest feedback.

Many thanks all and good luck!

Hi all, this is a message to all the designers.

Some good designs coming in but we're still after that something special for the website design. Keep the designs coming and please feel free to experiment with the design colours, layout etc.

The basic principle of the website needs to remain regarding the 12 products, search within block and 4 steps all appearing on the homepage.

The 4 steps seems to work best when it's got text as well as some simple images next to this.

A variation with the product titles with how to display this, some designers have gone with a simple white background whereas others have gone with colours. Please experiment here and where possible, add a contract / texture to the colour. Please remember the product titles needs to be clear, centured and with the circle tick box to the left of it. 

We're after a fairly simple design although we need it to look 21st century, up to date as well as interesting. The key points straight away are the 4 steps as well as the 12 products so try to guide the viewer to these areas a little.

White background behind the 12 images seems to be a much, although a light colour could possibly work.

The keypoints underneath these 12 products are too very important as it outlines what we do etc. Tick colour can vary.

Next to these keypoints will be the 'before' and 'after' images, these images needs to be fairly small and ensure there is white background around the image itself.

Good luck all and any questions, feel free to ask away.

Thanks!

Hi,

 Thank you for your time and effort with these designs, we are very nearly there with the design but we've thought of something that may work for the homepage. A curved arrow from step 1 pointing to the products, this may or may not work but feel free to give it a go.

Many thanks,

Thank you to everyone for your time and efforts with the design. It's hugely appreciated so thank you all once again.

Wish you all the luck in the future.

Trade

Serif
Sans Serif

```html
<!DOCTYPE html>
<html lang="en">
<head>
<meta charset="utf-8">
<title>Wrapfinder Hub – Find and Compare Vinyl Installers</title>
<link href="https://fonts.googleapis.com/css2?family=Roboto+Condensed:wght@400;700&family=Open+Sans:wght@400;600;700&family=Arimo:wght@400;700&display=swap" rel="stylesheet">
<style>
:root{
  --blue:#1b79cc;--blue-dark:#0f5ca3;--blue-light:#4fa3e6;
  --orange:#f07c13;--black:#0b0b0b;--ink:#222;--grey:#e6e6e6;
  --cream:#fdf5d6;--pill:#ebe3c6;--footer:#2f2f2f;--footer-text:#c9c9c9;
}
*{margin:0;padding:0;box-sizing:border-box}
html,body{width:706px;height:1200px;overflow:hidden;background:#fff}
body{position:relative;font-family:"Open Sans",Arial,sans-serif;color:var(--ink)}
.abs{position:absolute}
/* header */
.brand{left:83px;top:30px;display:flex;align-items:center;gap:8px}
.brand-dot{width:26px;height:26px;border-radius:50%;background:var(--orange)}
.brand-name{font-family:"Roboto Condensed",sans-serif;font-weight:700;font-size:26px;color:var(--blue-dark);letter-spacing:.5px}
.tagline{left:385px;top:40px;font-family:"Roboto Condensed",sans-serif;font-size:14px;line-height:16px;color:var(--blue-dark);text-transform:uppercase}
.map{left:478px;top:8px;width:145px;height:72px;background:linear-gradient(#e2e2e2,#cfcfcf);border-radius:14px}
/* nav */
.nav{left:0;top:88px;width:706px;height:24px;background:linear-gradient(#3a95e0,var(--blue) 50%,var(--blue-dark));}
.nav a{position:absolute;top:0;height:24px;line-height:24px;color:#fff;font-size:11px;font-weight:600;text-decoration:none;transform:translateX(-50%)}
.nav .active{background:var(--blue-light);width:70px;text-align:center}
/* steps */
.steps{left:0;top:112px;width:706px;height:193px;background:repeating-linear-gradient(90deg,#0b0b0b 0 6px,#151515 6px 8px)}
.step{position:absolute;background:#fff;box-shadow:0 0 6px rgba(0,0,0,.4);text-align:center}
.step::after{content:"";position:absolute;left:0;top:100%;width:100%;height:52px;background:linear-gradient(#7d7d7d,#1a1a1a)}
.step-num{position:absolute;left:2px;top:-6px;width:18px;height:16px;background:var(--orange);color:#fff;font-size:8px;font-weight:700;line-height:16px}
.step svg{display:block;margin:0 auto}
.step p{font-size:10.5px;line-height:13px;font-weight:600;color:#222;white-space:nowrap}
/* products */
.products{left:0;top:305px;width:706px;height:453px;background:#f8f8f8}
.tile{position:absolute;width:129px;height:130px;background:#fff;border:3px solid #e9e9e9}
.tile .photo{height:100px}
.tile span{display:block;height:24px;line-height:26px;background:var(--grey);font-size:10.5px;padding-left:3px;color:#222;white-space:nowrap;overflow:hidden}
/* keypoints */
.keys{left:0;top:758px;width:706px;height:287px;background:var(--cream)}
.point{position:absolute;left:83px;width:207px;height:28px;background:var(--pill);border-radius:14px;font-family:"Arimo",Arial,sans-serif;font-size:9.5px;line-height:28px;padding-left:22px;color:#111;white-space:nowrap;overflow:hidden}
.point::before{content:"";position:absolute;left:7px;top:9px;width:10px;height:10px;border-radius:50%;background:#fff}
.point::after{content:"";position:absolute;left:11px;top:12px;border:2px solid transparent;border-left:3px solid #333}
.label{position:absolute;width:153px;height:22px;background:var(--pill);text-align:center;font-family:"Roboto Condensed",sans-serif;font-size:14px;line-height:22px;color:#222}
.shot{position:absolute;width:153px;height:99px;background:#fff;border:1px solid #ddd;padding:3px}
.shot div{width:100%;height:100%}
/* footer */
.footer{left:0;top:1045px;width:706px;height:155px;background:var(--footer);color:var(--footer-text);font-size:8px;line-height:14px}
.footer h3{font-family:"Roboto Condensed",sans-serif;font-size:12px;color:#fff;font-weight:400;margin-bottom:5px}
.divider{position:absolute;top:0;width:1px;height:118px;background:#444}
.signup{width:173px;height:22px;background:#fff;border-radius:2px;font-size:7px;color:#555;line-height:22px;padding-left:6px;position:relative}
.go{position:absolute;right:5px;top:5px;width:12px;height:12px;border-radius:50%;background:var(--orange);color:#fff;font-size:6px;line-height:12px;text-align:center}
.social{display:flex;gap:4px;margin-top:10px}
.social i{width:20px;height:20px}
.copy{left:83px;top:118px;width:540px;border-top:1px solid #4a4a4a;text-align:center;padding-top:10px}
</style>
</head>
<body>
<header>
  <div class="abs brand"><span class="brand-dot"></span><span class="brand-name">WRAPFINDER HUB</span></div>
  <div class="abs map" role="img" aria-label="Grey dotted world map with red location pins"></div>
  <p class="abs tagline">Find a professional<br>vinyl installer today</p>
</header>
<nav class="abs nav">
  <a class="active" href="#" style="left:117px">HOME</a>
  <a href="#" style="left:205px">ABOUT US</a>
  <a href="#" style="left:291px">BLOG</a>
  <a href="#" style="left:421px">LIST YOUR COMPANY HERE</a>
  <a href="#" style="left:570px">CONTACT US</a>
</nav>
<section class="abs steps">
  <div class="step" style="left:83px;top:40px;width:129px;height:86px">
    <span class="step-num">01</span>
    <svg width="44" height="40" viewBox="0 0 44 40" style="margin-top:14px"><path d="M6 22 L16 32 L38 8" fill="none" stroke="#f07c13" stroke-width="7"/></svg>
    <p>Select Chosen<br>Product</p>
  </div>
  <div class="step" style="left:214px;top:35px;width:129px;height:96px">
    <span class="step-num">02</span>
    <svg width="40" height="36" viewBox="0 0 40 36" style="margin-top:6px"><circle cx="23" cy="14" r="9" fill="none" stroke="#f07c13" stroke-width="4"/><path d="M16 21 L7 32" stroke="#f07c13" stroke-width="5"/></svg>
    <p style="font-size:10px">Input Postcode, Distance</p>
    <svg width="14" height="14" viewBox="0 0 14 14"><path d="M7 0V14M0 7H14" stroke="#f07c13" stroke-width="4"/></svg>
    <p>Search</p>
  </div>
  <div class="step" style="left:345px;top:29px;width:136px;height:109px">
    <span class="step-num">03</span>
    <svg width="40" height="40" viewBox="0 0 40 40" style="margin-top:8px"><circle cx="20" cy="20" r="17" fill="none" stroke="#f07c13" stroke-width="4"/><text x="20" y="28" text-anchor="middle" font-size="22" font-weight="700" fill="#f07c13" font-family="Open Sans,sans-serif">$</text></svg>
    <p style="margin-top:6px">Compare Companies</p>
    <svg width="14" height="14" viewBox="0 0 14 14"><path d="M7 0V14M0 7H14" stroke="#f07c13" stroke-width="4"/></svg>
    <p>Prices</p>
  </div>
  <div class="step" style="left:483px;top:24px;width:139px;height:129px">
    <span class="step-num">04</span>
    <svg width="44" height="34" viewBox="0 0 44 34" style="margin-top:20px"><rect x="2" y="2" width="40" height="30" fill="#f07c13"/><path d="M2 2 L22 20 L42 2" fill="none" stroke="#fff" stroke-width="2"/></svg>
    <p style="margin-top:18px">Contact Chosen<br>Company</p>
  </div>
</section>
<main class="abs products">
  <div class="tile" style="left:83px;top:22px"><div class="photo" role="img" aria-label="Red car with colour change wrap" style="background:linear-gradient(#fff,#e23030 60%,#fff)"></div><span>Colour Change Wrap</span></div>
  <div class="tile" style="left:220px;top:22px"><div class="photo" role="img" aria-label="White van with printed sky and grass wrap" style="background:linear-gradient(#7fb7e6,#fff 55%,#5aa83a)"></div><span>Printed Vehicle Wrap</span></div>
  <div class="tile" style="left:357px;top:22px"><div class="photo" role="img" aria-label="Two green hatchbacks with tinted windows" style="background:linear-gradient(135deg,#fff,#3cb54a 50%,#fff)"></div><span>Window Tint</span></div>
  <div class="tile" style="left:494px;top:22px"><div class="photo" role="img" aria-label="Red sports car with tinted headlights at a show" style="background:linear-gradient(#c9c9c9,#b8202a 65%,#777)"></div><span>Headlight Tint</span></div>
  <div class="tile" style="left:83px;top:161px"><div class="photo" role="img" aria-label="White van with business signage" style="background:linear-gradient(#fff,#e8e8e8 70%,#bbb)"></div><span>Vehicle Signage</span></div>
  <div class="tile" style="left:220px;top:161px"><div class="photo" role="img" aria-label="Shop front with vinyl signage" style="background:linear-gradient(#ddd,#333 40%,#555 80%,#cfc6b8)"></div><span>Shop Signage</span></div>
  <div class="tile" style="left:357px;top:161px"><div class="photo" role="img" aria-label="Silver car with black vinyl roof" style="background:radial-gradient(circle,#555,#bcbcbc 40%,#fff 70%)"></div><span>Roof Vinyl Wrap</span></div>
  <div class="tile" style="left:494px;top:161px"><div class="photo" role="img" aria-label="Silver car with black vinyl bonnet" style="background:radial-gradient(circle,#444,#bcbcbc 40%,#fff 70%)"></div><span>Bonnet Vinyl Wrap</span></div>
  <div class="tile" style="left:83px;top:300px"><div class="photo" role="img" aria-label="Blue car with carbon fibre vinyl bonnet" style="background:linear-gradient(#a9a9a9,#2e3a6b 60%,#777)"></div><span>Carbon Fibre Vinyl</span></div>
  <div class="tile" style="left:220px;top:300px"><div class="photo" role="img" aria-label="White car with colourful stickerbomb bonnet" style="background:linear-gradient(#fff,#f2c230 35%,#e44 55%,#fff 80%)"></div><span>Stickerbomb Vinyl</span></div>
  <div class="tile" style="left:357px;top:300px"><div class="photo" role="img" aria-label="Orange sports car with clear protective film" style="background:linear-gradient(#8c9aa6,#f39a1c 60%,#555)"></div><span>Clear Protective Vinyl</span></div>
  <div class="tile" style="left:494px;top:300px"><div class="photo" role="img" aria-label="Black van with refurbished green wheels" style="background:linear-gradient(#888,#1a1a1a 50%,#7a7a7a)"></div><span>Wheel Refurb</span></div>
</main>
<section class="abs keys">
  <p class="point" style="top:22px">Lorem ipsum dolor sit amet, consectetur.</p>
  <p class="point" style="top:94px">Lorem ipsum dolor sit amet, consectetur.</p>
  <p class="point" style="top:166px">Lorem ipsum dolor sit amet, consectetur.</p>
  <p class="point" style="top:238px">Lorem ipsum dolor sit amet, consectetur.</p>
  <div class="label" style="left:305px;top:23px">BEFORE</div>
  <div class="label" style="left:470px;top:23px">AFTER</div>
  <div class="shot" style="left:305px;top:56px"><div role="img" aria-label="White car before wrapping" style="background:linear-gradient(#d8e2ea,#6f8a5a 35%,#f3f3f3 55%,#9b8a6e)"></div></div>
  <div class="shot" style="left:470px;top:56px"><div role="img" aria-label="White car after wrapping" style="background:linear-gradient(#8fb7e8,#4e7a3c 35%,#f5f5f5 55%,#8f8a6e)"></div></div>
  <div class="shot" style="left:305px;top:166px"><div role="img" aria-label="Worn alloy wheel before refurbishment" style="background:radial-gradient(circle,#777,#c7c7c7 45%,#333 80%)"></div></div>
  <div class="shot" style="left:470px;top:166px"><div role="img" aria-label="Refurbished alloy wheel" style="background:radial-gradient(circle,#888,#e2e2e2 45%,#555 80%)"></div></div>
</section>
<footer class="abs footer">
  <div class="abs" style="left:83px;top:16px">
    <h3>Contact Us</h3>
    <p><b>Wrapfinder Hub.</b><br>Phone: (123) 5550 1482<br>Fax:&nbsp; (123) 5550 1483<br>Email: hello@wrapfinderhub.com</p>
  </div>
  <span class="divider" style="left:240px"></span>
  <div class="abs" style="left:275px;top:16px">
    <h3>Sign Up for updates</h3>
    <div class="signup">Enter your email...<span class="go">Go</span></div>
    <div class="social"><i style="background:#3b5a98"></i><i style="background:#2ba0db"></i><i style="background:#d9412f"></i></div>
  </div>
  <span class="divider" style="left:490px"></span>
  <div class="abs" style="left:529px;top:16px">
    <h3>Quick Links</h3>
    <p>Home<br>About Us<br>Blog<br>List Your Company Here<br>Contact Us</p>
  </div>
  <p class="abs copy">Copyright © 2013 Wrapfinder Hub. All Rights Reserved.</p>
</footer>
</body>
</html>
```